QDL Kids Choir

Card to hand out or mail out with our own mailing labels. Needs to be appealing to families with children ages 4 yrs through 6th grade, who have an interest in musical experiences for the kids in a contemporary Bible teaching/church setting. We have 3 different kids choirs: 4-yr-old & Kindergarten Choir, 1st-3rd grade choir, and 4th-6th grade choir. This is a FREE after-school program every Tuesday from 3:30-5:00. Transportation for grades 1-6 from local schools is provided. Parents should expect their children to experience fun, friends, music, recreation, games, snacks, character building, Bible teaching, in an encouraging church environment.

Church

• Bight colors

```html
<!DOCTYPE html>
<html lang="en">
<head>
<meta charset="utf-8">
<title>QDL Kids Choir</title>
<link rel="stylesheet" href="https://fonts.googleapis.com/css2?family=Graduate&family=Squada+One&family=Kurale&family=Francois+One&family=Luckiest+Guy&family=Passion+One:wght@700&family=Kalam&display=swap">
<style>
  :root {
    --paper: #f8f4ec;
    --title-green: #5faf88;
    --title-edge: #7a4a32;
    --label-pink: #f3c8b6;
    --label-olive: #8d9a34;
    --label-ink: #6b4a3e;
    --teal: #4f9e80;
    --ticket-red: #e4415a;
    --ticket-edge: #d8233f;
    --slate-blue: #5d86a2;
    --band-green: #80b9a2;
    --band-ink: #e2385a;
    --white: #ffffff;
  }
  * { box-sizing: border-box; margin: 0; padding: 0; }
  html, body { width: 941px; height: 1200px; overflow: hidden; background: var(--paper); }
  .flyer { position: relative; width: 941px; height: 1200px; background: var(--paper); overflow: hidden; }

  .notes-art {
    position: absolute; left: 0; top: 0; width: 372px; height: 1200px;
    background:
      radial-gradient(ellipse at 30% 12%, rgba(160,200,70,.55), transparent 45%),
      radial-gradient(ellipse at 70% 25%, rgba(245,160,60,.5), transparent 45%),
      radial-gradient(ellipse at 25% 45%, rgba(250,205,70,.55), transparent 45%),
      radial-gradient(ellipse at 60% 62%, rgba(235,90,70,.45), transparent 45%),
      radial-gradient(ellipse at 35% 80%, rgba(80,130,210,.4), transparent 45%),
      linear-gradient(90deg, rgba(250,235,210,.9), rgba(248,244,236,0));
  }

  .site-title { position: absolute; left: 0; top: 0; font-size: 0; }
  .title-mark {
    position: absolute; text-align: center; white-space: nowrap;
    color: var(--title-green);
    -webkit-text-stroke: 1.5px var(--title-edge);
  }
  .title-initials { left: 400px; top: 52px; width: 360px; font: 148px/1 "Graduate", serif; letter-spacing: 2px; }
  .title-words {
    left: 350px; top: 230px; width: 500px;
    font: 120px/1 "Squada One", sans-serif; letter-spacing: 3px;
    transform: scaleY(1.3); transform-origin: top center;
  }

  .choir-label { position: absolute; left: 350px; top: 376px; width: 500px; height: 285px; }
  .choir-label svg { position: absolute; inset: 0; }
  .choir-list { position: absolute; left: 50px; top: 52px; color: var(--label-ink); font-family: "Kurale", serif; }
  .choir-list h2 { font-weight: 400; font-size: 31px; margin-bottom: 18px; margin-left: 10px; }
  .choir-list li { list-style: none; font-size: 24px; line-height: 40px; }

  .program-line {
    position: absolute; left: 329px; top: 684px; width: 560px; text-align: center;
    font: 36px/1 "Francois One", sans-serif; color: var(--teal); letter-spacing: 2px; text-transform: uppercase;
  }

  .schedule-ticket { position: absolute; left: 391px; top: 754px; width: 423px; height: 128px; }
  .schedule-ticket svg { position: absolute; inset: 0; }
  .schedule-text {
    position: absolute; inset: 0; display: flex; flex-direction: column; align-items: center; justify-content: center;
    color: var(--white); font-family: "Luckiest Guy", "Passion One", sans-serif; transform: rotate(-4deg);
  }
  .schedule-day { font-size: 34px; line-height: 1.1; }
  .schedule-time { font-size: 54px; line-height: 1; }

  .transport-note {
    position: absolute; left: 343px; top: 928px; width: 520px; text-align: center;
    font: 700 33px/1.2 "Passion One", sans-serif; color: var(--slate-blue);
  }

  .dot-strip {
    position: absolute; left: 0; top: 1034px; width: 941px; height: 30px;
    background: linear-gradient(90deg, #f2c744, #e0486a, #8fbf5a, #9bd2c8, #f2c744, #e0486a, #8fbf5a, #9bd2c8);
    opacity: .75;
  }
  .promise-band {
    position: absolute; left: 0; top: 1064px; width: 941px; height: 92px;
    background: var(--band-green); border-bottom: 8px dotted var(--white);
    display: flex; align-items: center; justify-content: center; text-align: center;
    padding: 0 30px 8px;
  }
  .promise-band p { font: 22px/1.25 "Kalam", cursive; color: var(--band-ink); }
</style>
</head>
<body>
<main class="flyer">
  <div class="notes-art" role="img" aria-label="Cascade of colourful music notes and clefs in yellow, orange, green, red and blue"></div>

  <h1 class="site-title">
    <span class="title-mark title-initials">QDL</span>
    <span class="title-mark title-words">KIDS CHOIR</span>
  </h1>

  <section class="choir-label">
    <svg viewBox="0 0 500 285" width="500" height="285" aria-hidden="true">
      <path d="M30 8 H470 Q470 30 492 30 V255 Q470 255 470 277 H30 Q30 255 8 255 V30 Q30 30 30 8 Z"
            fill="var(--label-pink)" stroke="var(--label-olive)" stroke-width="5"/>
      <path d="M38 18 H462 Q462 38 482 38 V247 Q462 247 462 267 H38 Q38 247 18 247 V38 Q38 38 38 18 Z"
            fill="none" stroke="var(--label-ink)" stroke-width="1.2" stroke-dasharray="4 4"/>
    </svg>
    <div class="choir-list">
      <h2>Three different kids choirs:</h2>
      <ul>
        <li>1) 4-yr-old &amp; Kindergarten Choir</li>
        <li>2) 1st-3rd grade choir</li>
        <li>3) 4th-6th grade choir</li>
      </ul>
    </div>
  </section>

  <p class="program-line">Free after-school program</p>

  <section class="schedule-ticket">
    <svg viewBox="0 0 423 128" width="423" height="128" aria-hidden="true">
      <rect x="4" y="4" width="415" height="120" rx="22" fill="var(--ticket-edge)"/>
      <rect x="26" y="12" width="371" height="104" rx="16" fill="var(--ticket-red)" stroke="#f7a0ae" stroke-width="1.5" stroke-dasharray="4 3" transform="rotate(-3 211 64)"/>
    </svg>
    <div class="schedule-text">
      <span class="schedule-day">every Tuesday from:</span>
      <span class="schedule-time">3:30-5:00</span>
    </div>
  </section>

  <p class="transport-note">Transportation for grades 1-6<br>from local schools IS PROVIDED!!!</p>

  <div class="dot-strip" role="img" aria-label="Row of colourful ring dots"></div>
  <footer class="promise-band">
    <p>Experience Fun, Friends, Music, Recreation, Games, Snacks,<br>Character Building, Bible Teaching, In An Encouraging Church Environment.</p>
  </footer>
</main>
</body>
</html>
```